MOLVT Study flyer

I need help designing a flyer for a research study that will include brain imaging in adolescents. The info is in the attached document. The study is called the Marrowby Orchard Lantern Vesper Trail (MOLVT) study. Ideally this would be returned as a document that I can edit in the future as we will have several new recruitment phases (different age groups, etc. I also would love to have a logo designed as part of this project, but I recognize that might be a separate design request.

```html
<!DOCTYPE html>
<html lang="en">
<head>
<meta charset="utf-8">
<title>MOLVT Study Flyer</title>
<link href="https://fonts.googleapis.com/css2?family=Poppins:wght@500;600;700;800&family=Inter:wght@400;500;600&display=swap" rel="stylesheet">
<style>
  :root {
    --navy: #1f2a5c;
    --teal: #3d8f98;
    --purple: #8a1fb8;
    --ink: #2f2f35;
    --muted: #4a4a52;
    --card: #f3f2f7;
    --eligible: #e8f1f4;
    --rule: #c9c9d0;
    --coral: #f4b8a6;
    --white: #ffffff;
  }
  * { box-sizing: border-box; margin: 0; padding: 0; }
  html, body { width: 848px; height: 1200px; overflow: hidden; background: var(--white); }
  .flyer { position: relative; width: 848px; height: 1200px; overflow: hidden; font-family: "Inter", sans-serif; color: var(--ink); }

  .hero-image {
    position: absolute; right: 0; top: 0; width: 300px; height: 530px;
    background:
      radial-gradient(circle at 62% 18%, rgba(170,120,255,.75), rgba(90,70,200,.35) 28%, transparent 48%),
      radial-gradient(ellipse at 70% 55%, #2c3f70 0%, #5e86a6 45%, rgba(190,215,228,.6) 70%, transparent 85%);
  }

  .brand-mark { position: absolute; left: 70px; top: 48px; width: 150px; height: 150px; border-radius: 50%; background: var(--eligible); }
  .brand { position: absolute; left: 270px; top: 36px; width: 300px; text-align: center; }
  .brand-name { font-family: "Poppins", sans-serif; font-weight: 800; font-size: 104px; line-height: 1; color: var(--navy); letter-spacing: -1px; }
  .brand-tag { display: flex; align-items: center; gap: 12px; margin-top: 0; font-family: "Poppins", sans-serif; font-weight: 800; font-size: 38px; letter-spacing: 10px; color: var(--navy); line-height: 1.1; }
  .brand-tag::before, .brand-tag::after { content: ""; flex: 1; height: 4px; background: var(--navy); }
  .brand-sub { margin-top: 12px; font-family: "Inter", sans-serif; font-size: 20px; line-height: 26px; color: var(--muted); }

  .headline { position: absolute; left: 57px; top: 282px; font-family: "Poppins", sans-serif; font-weight: 700; font-size: 26px; line-height: 34px; color: var(--ink); }
  .headline em { font-style: normal; color: var(--purple); }
  .intro { position: absolute; left: 57px; top: 374px; width: 560px; font-size: 18.5px; line-height: 25px; color: var(--ink); }

  .section-title { position: absolute; left: 57px; top: 502px; width: 734px; display: flex; align-items: center; gap: 14px; font-family: "Poppins", sans-serif; font-weight: 600; font-size: 23px; color: var(--purple); }
  .section-title::before { content: ""; flex: 1; height: 1px; background: var(--rule); }
  .section-title::after { content: ""; flex: 1; height: 1px; background: var(--rule); }

  .step { position: absolute; background: var(--card); border-radius: 12px; display: flex; align-items: center; gap: 22px; padding: 0 28px; font-size: 17px; line-height: 23px; color: var(--ink); }
  .step svg { flex: none; }
  .step-interview { left: 57px; top: 551px; width: 395px; height: 123px; }
  .step-survey { left: 474px; top: 551px; width: 317px; height: 123px; }
  .step-visit { left: 57px; top: 695px; width: 734px; height: 124px; }

  .eligibility { position: absolute; left: 57px; top: 841px; width: 734px; height: 132px; background: var(--eligible); border-radius: 12px; padding: 16px 38px; }
  .eligibility h2 { font-family: "Poppins", sans-serif; font-weight: 600; font-size: 25px; color: var(--teal); margin-bottom: 6px; }
  .eligibility ul { padding-left: 20px; font-size: 16.5px; line-height: 21px; }

  .contact { position: absolute; left: 57px; top: 1009px; width: 734px; height: 142px; background: var(--navy); border-radius: 14px; padding: 28px 38px; color: var(--white); }
  .contact-lead { font-family: "Poppins", sans-serif; font-weight: 600; font-size: 23px; line-height: 29px; }
  .contact-email { display: flex; align-items: center; gap: 12px; margin-top: 8px; font-family: "Poppins", sans-serif; font-weight: 600; font-size: 22px; color: var(--coral); }
  .compensation { position: absolute; left: 534px; top: 996px; width: 254px; height: 155px; background: var(--teal); color: var(--white); text-align: center; padding-top: 22px; font-family: "Poppins", sans-serif; font-weight: 700; }
  .compensation-label { font-size: 22px; line-height: 28px; }
  .compensation-amount { font-size: 58px; line-height: 62px; }
</style>
</head>
<body>
<div class="flyer">
  <div class="hero-image" role="img" aria-label="Profile of a young girl with a glowing brain and network lines"></div>

  <div class="brand-mark"></div>
  <div class="brand">
    <div class="brand-name">MOLVT</div>
    <div class="brand-tag">STUDY</div>
    <p class="brand-sub">Marrowby Orchard Lantern<br>Vesper Trail</p>
  </div>

  <h1 class="headline">Are You The Parent Of A Child Age 10-17?<br>Do They <em>Worry</em> Or <em>Overthink Negative Emotions?</em></h1>
  <p class="intro">Halvergate University researchers are seeking girls age 10-17 for a study about brain activity in emotions and decision-making and how they relate to puberty, anxiety and depression.</p>

  <div class="section-title">Study Participation Involves</div>

  <div class="step step-interview">
    <svg width="48" height="44" viewBox="0 0 48 44" aria-hidden="true">
      <path d="M4 4h24a4 4 0 0 1 4 4v12a4 4 0 0 1-4 4H14l-8 7v-7H4a4 4 0 0 1-4-4V8a4 4 0 0 1 4-4z" fill="#1a1a1a"/>
      <path d="M22 18h20a4 4 0 0 1 4 4v10a4 4 0 0 1-4 4h-2v7l-8-7H22a4 4 0 0 1-4-4V22a4 4 0 0 1 4-4z" fill="#1a1a1a" stroke="#f3f2f7" stroke-width="3"/>
      <rect x="25" y="24" width="16" height="3" fill="#f3f2f7"/><rect x="25" y="29" width="12" height="3" fill="#f3f2f7"/>
    </svg>
    <p>One one-hour interview (online or in-person) where your child will discuss their thoughts</p>
  </div>

  <div class="step step-survey">
    <svg width="52" height="44" viewBox="0 0 52 44" aria-hidden="true">
      <rect x="2" y="2" width="48" height="32" rx="3" fill="#1a1a1a"/>
      <rect x="8" y="8" width="10" height="3" fill="#f3f2f7"/><rect x="8" y="14" width="10" height="3" fill="#f3f2f7"/><rect x="8" y="20" width="10" height="3" fill="#f3f2f7"/>
      <rect x="24" y="8" width="20" height="20" fill="#f3f2f7"/><circle cx="34" cy="15" r="4" fill="#1a1a1a"/><rect x="28" y="21" width="12" height="6" rx="3" fill="#1a1a1a"/>
      <rect x="20" y="36" width="12" height="4" fill="#1a1a1a"/><rect x="14" y="40" width="24" height="3" fill="#1a1a1a"/>
    </svg>
    <p>Online questionnaires (parent and child)</p>
  </div>

  <div class="step step-visit">
    <svg width="44" height="44" viewBox="0 0 44 44" aria-hidden="true">
      <circle cx="12" cy="22" r="10" fill="#1a1a1a"/>
      <path d="M28 14a10 10 0 0 1 0 16" fill="none" stroke="#1a1a1a" stroke-width="3" stroke-linecap="round"/>
      <path d="M34 9a17 17 0 0 1 0 26" fill="none" stroke="#1a1a1a" stroke-width="3" stroke-linecap="round"/>
    </svg>
    <p>One two-hour visit where your child will complete an MRI scan, answer questions about their puberty stage, and have a small hair sample taken to study puberty hormones</p>
  </div>

  <section class="eligibility">
    <h2>Your Child May Be Eligible If They</h2>
    <ul>
      <li>Are age 10-17</li>
      <li>Tend to worry or overthink negative thoughts</li>
      <li>have not been diagnosed with psychosis, learning problems, or autism</li>
    </ul>
  </section>

  <section class="contact">
    <p class="contact-lead">INTERESTED IN PARTICIPATING?<br>WANT MORE INFORMATION?</p>
    <p class="contact-email">
      <svg width="26" height="20" viewBox="0 0 26 20" aria-hidden="true"><rect width="26" height="20" rx="2" fill="#ffffff"/><path d="M2 3l11 8 11-8" fill="none" stroke="#1f2a5c" stroke-width="2.5"/></svg>
      molvtstudy@halvergate.edu
    </p>
  </section>
  <div class="compensation">
    <div class="compensation-label">COMPENSATION<br>UP TO</div>
    <div class="compensation-amount">$140</div>
  </div>
</div>
</body>
</html>
```